Korvatch Law Rebrand

I am recreating my law firm website. I got a new logo and would like to recreate the website to match the new logo. the website is korvatchlaw.com

```html
<!DOCTYPE html>
<html lang="en">
<head>
<meta charset="utf-8">
<title>Korvatch Law, PLLC</title>
<link rel="stylesheet" href="https://fonts.googleapis.com/css2?family=Poppins:ital,wght@0,300;0,400;0,500;1,500&family=Great+Vibes&display=swap">
<style>
:root{
  --navy:#0b4a8c;
  --navy-deep:#0a3f7a;
  --ink:#2b2f36;
  --muted:#6b7079;
  --pale:#f2f4f8;
  --bar:#9aa9c8;
  --white:#ffffff;
  --link:#7fb0ff;
}
*{margin:0;padding:0;box-sizing:border-box}
html,body{width:1200px;height:3699px;overflow:hidden}
body{font-family:"Poppins",sans-serif;color:var(--ink);background:var(--pale);position:relative}
.abs{position:absolute}
.skew-btn{position:absolute;display:flex;align-items:center;justify-content:center;font-size:17px;font-weight:500;letter-spacing:.2px;isolation:isolate;z-index:1}
.skew-btn::before{content:"";position:absolute;inset:0;transform:skewX(-14deg);z-index:-1}
.btn-blue{color:var(--white)}
.btn-blue::before{background:var(--navy)}
.btn-white{color:var(--ink)}
.btn-white::before{background:var(--white)}

/* hero */
.hero{left:0;top:0;width:1200px;height:727px;background:linear-gradient(180deg,#4f79a8 0%,#8aa7c3 35%,#b8a58c 62%,#6d7560 100%);isolation:isolate}
.brand{position:absolute;display:flex;align-items:center;gap:10px;font-weight:500;letter-spacing:3px}
.brand .mark{width:16px;height:16px}
.hero .brand{left:110px;top:50px;color:var(--white);font-size:26px}
.hero .brand .mark{background:var(--white)}
.nav{position:absolute;left:398px;top:40px;display:flex;gap:24px;font-size:18px;color:var(--white)}
.nav .on{color:var(--link)}
.hero h1{position:absolute;left:0;width:1200px;top:172px;text-align:center;color:var(--white);font-weight:400;font-size:48px;line-height:64px}

/* about */
.about{left:0;top:727px;width:1200px;height:827px;background:var(--pale);isolation:isolate}
.iam{left:100px;top:85px;font-family:"Great Vibes",cursive;font-size:34px;line-height:1;color:var(--navy)}
.sig{left:145px;top:120px;font-family:"Great Vibes",cursive;font-size:60px;line-height:1;color:var(--navy);transform:rotate(-7deg);transform-origin:left bottom;white-space:nowrap}
.portrait{left:0;top:210px;width:578px;height:617px;background:linear-gradient(180deg,#e7ebf2 0%,#c9b8a6 40%,#26324a 80%,#1d2738 100%)}
.about h2{left:620px;top:95px;font-weight:400;font-size:40px;line-height:51px}
.about .copy{left:620px;top:233px;width:485px;font-size:16.5px;line-height:28.5px;color:var(--muted);font-weight:300}
.about .copy p{margin-bottom:28px}

/* practice */
.practice{left:0;top:1554px;width:1200px;height:944px;background:linear-gradient(180deg,var(--pale) 0%,#eef0f4 60%,#e6e4e2 100%)}
.section-title{position:absolute;left:0;width:1200px;text-align:center;font-weight:400}
.practice .section-title{top:85px;font-size:37px}
.card{position:absolute;width:250px;text-align:center}
.card svg{display:block;margin:0 auto}
.card h3{font-weight:400;font-size:22px;margin:30px 0 22px}
.card p{font-size:16px;line-height:26.5px;color:var(--muted);font-weight:300;padding:0 4px}

/* blog */
.blog{left:0;top:2498px;width:1200px;height:670px;background:linear-gradient(120deg,#0c4e93 0%,#0a4583 100%)}
.blog .section-title{top:74px;font-size:38px;color:var(--white)}
.post{position:absolute;top:169px;width:310px;color:var(--white)}
.post .img{height:203px;clip-path:polygon(4% 0,100% 0,96% 100%,0 100%)}
.post .date{position:absolute;left:30px;top:178px;background:#7b8fb4;font-size:15px;padding:5px 12px}
.post h3{font-weight:500;font-size:21px;line-height:31px;margin-top:46px}
.post em{display:block;font-size:16px;font-weight:500;margin-top:2px}
.post p{font-size:16px;line-height:27px;font-weight:300;margin-top:26px}

/* footer */
.footer{left:0;top:3168px;width:1200px;height:444px;background:var(--pale)}
.footer .brand{left:110px;top:170px;color:var(--navy);font-size:36px}
.footer .brand .mark{width:22px;height:22px;background:var(--navy)}
.notify{left:113px;top:288px;font-size:16px;color:#444}
.signup{left:110px;top:332px;width:430px;height:53px;background:var(--white);display:flex;box-shadow:0 2px 8px rgba(0,0,0,.06)}
.signup span{flex:1;padding:16px;font-size:16px;color:#555}
.signup b{position:relative;width:88px;display:flex;align-items:center;justify-content:center;color:var(--white);font-weight:500;font-size:16px;isolation:isolate}
.signup b::before{content:"";position:absolute;inset:0 0 0 6px;background:var(--navy);transform:skewX(-10deg);z-index:-1}
.col h4{font-weight:400;font-size:20px;margin-bottom:20px}
.col li{list-style:none;font-size:16px;color:#444;height:36px}
.contact li{display:flex;gap:8px;height:auto;margin-bottom:24px;line-height:26px}
.contact svg{flex:none;margin-top:5px}

/* bottom bar */
.bottombar{left:0;top:3612px;width:1200px;height:87px;background:var(--bar);color:var(--white)}
.bottombar .copy{left:110px;top:32px;font-size:16px}
.social{right:110px;top:23px;display:flex;gap:10px}
.social span{width:40px;height:40px;border:1.5px solid var(--white);border-radius:50%}
</style>
</head>
<body>

<section class="abs hero" role="img" aria-label="City skyline photograph behind the headline">
  <div class="brand"><span class="mark"></span>KORVATCH LAW</div>
  <nav class="nav"><span class="on">Home</span><span>Practices Areas</span><span>About Me</span><span>Blog</span></nav>
  <a class="skew-btn btn-blue" style="left:822px;top:27px;width:268px;height:55px">SCHEDULE A CONSULTATION</a>
  <h1>PERSONAL LEGAL SOLUTION<br>IN LIFE'S MOST DIFFICULT MOMENTS</h1>
  <a class="skew-btn btn-white" style="left:463px;top:333px;width:275px;height:53px">SCHEDULE A CONSULTATION</a>
</section>

<section class="abs about">
  <div class="abs iam">I am</div>
  <div class="abs sig">Daniel Korvatch</div>
  <div class="abs portrait" role="img" aria-label="Portrait of the attorney in a navy suit and red tie"></div>
  <h2 class="abs">ATTORNEY AT<br>KORVATCH LAW PLLC</h2>
  <div class="abs copy">
    <p>It is my honor to provide quality legal services at a reasonable price to clients that I enjoy working with and for. I am grateful for all my clients and the trust they place in me to represent them.</p>
    <p>My practice focuses on Probate, Adult Guardianships, and Trust Administration and Litigation. I also represent clients in other general civil litigation matters.&nbsp; Finally, I handle estate planning for families of modest means.</p>
    <p>As your attorney, I would educate you about the law as it pertains to your situation, guide you through your options, and then help you to achieve your desired objectives from those options</p>
  </div>
  <a class="skew-btn btn-blue" style="left:608px;top:674px;width:272px;height:54px">SCHEDULE A CONSULTATION</a>
</section>

<section class="abs practice">
  <h2 class="section-title">PRACTICE AREAS</h2>
  <div class="card" style="left:107px;top:273px">
    <svg width="245" height="220" role="img" aria-label="Handshake with shield icon"><polygon points="0,0 245,0 122.5,220" fill="#fff"/><circle cx="122" cy="75" r="34" fill="#dbe4f0"/></svg>
    <h3>Probate and Trusts</h3>
    <p>Guiding clients through the legal process of administering a deceased person's estate, ensuring that assets are distributed according to their wishes while addressing any legal complexities that may arise.</p>
  </div>
  <div class="card" style="left:351px;top:171px">
    <svg width="245" height="220" role="img" aria-label="Hand holding house and money icon"><polygon points="122.5,0 245,220 0,220" fill="#fff"/><circle cx="122" cy="145" r="34" fill="#dbe4f0"/></svg>
    <h3>Estate Planning</h3>
    <p>Helping individuals and families create tailored plans that safeguard their assets, ensure their wishes are fulfilled, and provide for their loved ones after they pass away.</p>
  </div>
  <div class="card" style="left:599px;top:273px">
    <svg width="245" height="220" role="img" aria-label="Hands protecting a person icon"><polygon points="0,0 245,0 122.5,220" fill="#fff"/><circle cx="122" cy="75" r="34" fill="#dbe4f0"/></svg>
    <h3>Adult Guardianships</h3>
    <p>Assisting families in securing legal guardianship for individuals who are unable to make decisions for themselves, ensuring that their rights and well-being are protected through compassionate and effective representation.</p>
  </div>
  <div class="card" style="left:842px;top:171px">
    <svg width="245" height="220" role="img" aria-label="Two people with exchange arrows icon"><polygon points="122.5,0 245,220 0,220" fill="#fff"/><circle cx="122" cy="145" r="34" fill="#dbe4f0"/></svg>
    <h3>Civil Litigation</h3>
    <p>Representing clients in legal disputes, advocating for their rights and interests in various matters such as contract disputes, personal injury claims, and property issues, with a focus on achieving favorable outcomes through negotiation or trial.</p>
  </div>
</section>

<section class="abs blog">
  <h2 class="section-title">OUR BLOG</h2>
  <article class="post" style="left:110px">
    <div class="img" role="img" aria-label="Hand signing a document" style="background:linear-gradient(135deg,#cfd4db,#8f97a3)"></div>
    <span class="date">Sep 29</span>
    <h3>Trusts vs. Wills<em>Understanding the Differences</em></h3>
    <p>When it comes to estate planning, two of the most common tools are trusts and wills.</p>
  </article>
  <article class="post" style="left:445px">
    <div class="img" role="img" aria-label="Elderly couple signing papers" style="background:linear-gradient(135deg,#c9b9a8,#7e7468)"></div>
    <span class="date">Sep 21</span>
    <h3>Why probate is needed,...<br>sometimes</h3>
    <p>When it comes to estate planning, two of the most common tools are trusts and wills.</p>
  </article>
  <article class="post" style="left:778px">
    <div class="img" role="img" aria-label="People reviewing documents at a desk" style="background:linear-gradient(135deg,#b9bfc8,#6d6f75)"></div>
    <span class="date">Sep 15</span>
    <h3>Estate Planning<br>Essentials</h3>
    <p>Estate planning is often an overlooked aspect of financial management, yet it is crucial for ensuring..</p>
  </article>
</section>

<footer class="abs footer">
  <div class="brand"><span class="mark"></span>KORVATCH LAW</div>
  <div class="abs notify">We will notify you of any important news</div>
  <div class="abs signup"><span>Email Address</span><b>SEND</b></div>
  <div class="abs col" style="left:619px;top:88px">
    <h4>Quick Links</h4>
    <ul><li>Home</li><li>About Us</li><li>Practice Area</li><li>Blog</li><li>Contact</li></ul>
  </div>
  <div class="abs col contact" style="left:842px;top:88px">
    <h4>Contact Information</h4>
    <ul>
      <li><svg width="12" height="12" viewBox="0 0 24 24"><path fill="#0b4a8c" d="M6.6 10.8a15 15 0 006.6 6.6l2.2-2.2a1 1 0 011-.25 11 11 0 003.6.6 1 1 0 011 1V20a1 1 0 01-1 1A17 17 0 013 4a1 1 0 011-1h3.5a1 1 0 011 1 11 11 0 00.6 3.6 1 1 0 01-.25 1z"/></svg>(512) 555-0148</li>
      <li><svg width="10" height="14" viewBox="0 0 10 14"><path fill="#0b4a8c" d="M5 0a5 5 0 015 5c0 3.5-5 9-5 9S0 8.5 0 5a5 5 0 015-5zm0 3a2 2 0 100 4 2 2 0 000-4z"/></svg>245 Maple Avenue Suite B<br>Riverton, Texas 77410</li>
      <li><svg width="13" height="13" viewBox="0 0 14 14"><circle cx="7" cy="7" r="5.8" fill="none" stroke="#0b4a8c" stroke-width="2"/><path d="M7 4v3.3l2 1.3" fill="none" stroke="#0b4a8c" stroke-width="1.6"/></svg>Mon - Fri&nbsp; 8AM - 5PM</li>
    </ul>
  </div>
</footer>

<div class="abs bottombar">
  <div class="abs copy">© 2025 Korvatch Law, PLLC | All Rights Reserved</div>
  <div class="abs social" aria-label="Social links"><span></span><span></span><span></span></div>
</div>

</body>
</html>
```